Velmorra Design Group Business Card Design

We need a double-sided business card for our company Velmorra Design Group. Our slogan is "Simple Online Solutions." We are looking for a techy, cutting-edge but simple card that looks modern and sleek. We have a black logo attached and would prefer a lighter background to make our logo stand out. We like nice accents to make it pop out and make our clients remember our card.

On the back side, we just want our logo, slogan and website. Again, something very simple. Make the logo big on the back.

```html
<!DOCTYPE html>
<html lang="en">
<head>
<meta charset="utf-8">
<title>Velmorra Design Group – Business Card</title>
<link href="https://fonts.googleapis.com/css2?family=Exo+2:wght@400;500&display=swap" rel="stylesheet">
<style>
  :root {
    --stage: #c3c9c6;
    --card-light: #f4f5f4;
    --card-mid: #dfe2e0;
    --card-shade: #b9bdbb;
    --band: rgba(255, 255, 255, 0.88);
    --ink: #1c1c1c;
  }
  html, body {
    margin: 0;
    padding: 0;
    width: 1200px;
    height: 848px;
    overflow: hidden;
    background: var(--stage);
  }
  .canvas {
    position: relative;
    width: 1200px;
    height: 848px;
    background: var(--stage);
    font-family: "Exo 2", sans-serif;
    color: var(--ink);
  }
  .card {
    position: absolute;
    left: 346px;
    width: 530px;
    height: 325px;
    overflow: hidden;
    background: var(--card-light);
  }
  .card--front { top: 77px; }
  .card--back { top: 462px; }
  .card__pattern {
    position: absolute;
    inset: 0;
    background:
      linear-gradient(135deg, var(--card-light) 0%, var(--card-mid) 40%, var(--card-light) 60%, var(--card-shade) 100%);
  }
  .card__band {
    position: absolute;
    left: 0;
    right: 0;
    top: 107px;
    height: 91px;
    background: var(--band);
  }
  .front__name {
    position: absolute;
    right: 82px;
    top: 132px;
    margin: 0;
    font-size: 34px;
    font-weight: 400;
    letter-spacing: -0.3px;
    line-height: 1;
    white-space: nowrap;
  }
  .front__slogan {
    position: absolute;
    right: 83px;
    top: 180px;
    margin: 0;
    font-size: 14px;
    font-weight: 500;
    letter-spacing: 1.2px;
    line-height: 1;
    white-space: nowrap;
  }
  .back__web {
    position: absolute;
    left: 0;
    right: 0;
    top: 127px;
    margin: 0;
    text-align: center;
    font-size: 22px;
    font-weight: 400;
    letter-spacing: 1.6px;
    line-height: 1;
    white-space: nowrap;
  }
  .back__phone {
    position: absolute;
    left: 0;
    right: 0;
    top: 166px;
    margin: 0;
    text-align: center;
    font-size: 18px;
    font-weight: 400;
    letter-spacing: 2px;
    line-height: 1;
    white-space: nowrap;
  }
</style>
</head>
<body>
<main class="canvas">
  <section class="card card--front" aria-label="Card front">
    <div class="card__pattern" role="img" aria-label="Soft grey faceted diamond background pattern"></div>
    <div class="card__band"></div>
    <h1 class="front__name">Velmorra Design Group</h1>
    <p class="front__slogan">Simple Online Solutions</p>
  </section>

  <section class="card card--back" aria-label="Card back">
    <div class="card__pattern" role="img" aria-label="Soft grey faceted diamond background pattern"></div>
    <div class="card__band"></div>
    <p class="back__web">www.Velmorra Design Group</p>
    <p class="back__phone">000 000 00 00</p>
  </section>
</main>
</body>
</html>
```